Hensby Estates Website and Logo Design

We need a new logo and website designed for 'Hensby Estates Ltd', which is a well established Guernsey property holding company founded in 1934.

The company does not currently have a website. The new website should be similar in style and layout to https://www.corvanhale.org/.

Target Market(s)

Industry, Media, Tenants

Industry/Entity Type

Property Management

Logo Text

HEL OR Hensby Estates Ltd OR HE

Coding

Coded - Design and coding required

Number of Pages Required

4 page

Font styles to use
Other font styles liked:
• Helvetica

Requirements
Must have
• The logo laying over the picture (like https://www.corvanhale.org/).
• Big pictures on homepage (like https://www.corvanhale.org/)

```html
<!DOCTYPE html>
<html lang="en">
<head>
<meta charset="utf-8">
<title>Hensby Estates Limited</title>
<link href="https://fonts.googleapis.com/css2?family=Arimo:wght@400;700&display=swap" rel="stylesheet">
<style>
:root{
  --blue:#4f84d6;
  --blue-dark:#2e4470;
  --navy:#23385f;
  --ink:#222;
  --text:#666;
  --page:#f8f8f8;
  --white:#fff;
  --footer:#262626;
  --bar:#111;
}
*{box-sizing:border-box;margin:0;padding:0}
html,body{width:1200px;height:2875px;overflow:hidden}
body{background:var(--page);font-family:Arimo,Helvetica,Arial,sans-serif;color:var(--ink);position:relative}
section,header,footer{position:absolute;left:0;width:1200px}
.abs{position:absolute}
.center{text-align:center;left:0;width:1200px}
.btn{position:absolute;background:var(--blue);color:var(--white);font-size:13px;display:flex;align-items:center;justify-content:center;border:1px solid #7fa6e6}
.divider{position:absolute;left:535px;width:130px;height:10px}
.divider::before{content:"";position:absolute;left:0;right:0;top:4px;height:2px;background:#9db9e6}
.divider::after{content:"";position:absolute;left:58px;top:0;width:14px;height:10px;border:2px solid #9db9e6;border-radius:5px;background:var(--page)}

/* hero */
.hero{top:0;height:479px;background:linear-gradient(180deg,#3f5e9a 0%,#4a6aa4 35%,#3c5a8f 65%,#2f4a7c 100%)}
.logo{left:157px;top:22px;color:var(--white);font-weight:700;font-size:19px;line-height:23px}
.logo span{display:block;padding-left:36px}
.burger{left:1025px;top:34px;width:20px}
.burger i{display:block;height:3px;background:var(--white);margin-bottom:4px}
.slide-arrow{top:210px;width:22px;height:56px;background:rgba(255,255,255,.9)}
.hero-line1{top:224px;color:var(--white);font-size:21px}
.hero-line2{top:252px;color:var(--white);font-size:32px;font-weight:700}

/* about */
.about{top:479px;height:297px}
.section-title{font-size:25px;color:var(--ink)}
.body-text{font-size:12.5px;line-height:16px;color:var(--text)}

/* bands */
.band{color:var(--white)}
.band .section-title{color:var(--white)}
.band .body-text{color:var(--white)}
.why{top:776px;height:223px;background:linear-gradient(180deg,#2f4670 0%,#3d5a8c 55%,#283d63 100%)}
.blog-band{top:1236px;height:227px;background:linear-gradient(180deg,#5a7aae 0%,#3f6096 45%,#2b4a7a 100%)}
.notch{position:absolute;left:556px;width:96px;height:32px}

/* eras */
.eras{top:999px;height:237px}
.era{position:absolute;top:60px;width:300px;text-align:center}
.era h3{font-size:21px;font-weight:400;color:var(--ink)}
.era .dots{width:34px;margin:6px auto 16px;border-top:2px dotted var(--blue)}
.era p{font-size:11.5px;line-height:16px;color:var(--text);padding:0 8px}
.more{display:flex;align-items:center;justify-content:center;gap:8px;font-size:12px;color:var(--ink);margin-top:18px}
.more.link{color:var(--blue);text-decoration:underline}
.more.left{justify-content:flex-start}

/* posts */
.posts{top:1495px;height:1000px}
.card{position:absolute;top:33px;width:280px;height:395px;background:var(--white);box-shadow:0 0 6px rgba(0,0,0,.15);padding:9px}
.card .photo{height:197px;position:relative}
.date{position:absolute;left:16px;bottom:0;width:44px;height:44px;background:var(--blue);color:var(--white);font-weight:700;font-size:14px;line-height:17px;text-align:center;padding-top:5px}
.card h4,.event h4{font-size:15.5px;font-weight:400;color:var(--ink);margin:20px 0 10px}
.meta{display:flex;align-items:center;gap:6px;font-size:11.5px;color:#555}
.card p,.event p{font-size:11.5px;line-height:17px;color:var(--text);margin-top:12px}
.card .more,.event .more{margin-top:18px}
.events-title{top:470px}
.event{position:absolute;top:548px;width:433px}
.event .photo{height:203px;position:relative}
.event-date{position:absolute;left:157px;bottom:0;width:106px;height:20px;background:var(--blue);color:var(--white);font-size:11px;display:flex;align-items:center;justify-content:center}
.event h4{margin:20px 16px 10px}
.event .meta,.event p,.event .more{margin-left:16px;margin-right:16px}
.pager{top:922px;display:flex;justify-content:center;gap:4px;align-items:center;font-size:15px}

/* contact */
.contact{top:2473px;height:355px;background:linear-gradient(180deg,#3a3a3a 0%,#2a2a2a 50%,#1e1e1e 100%);color:var(--white)}
.contact .section-title{color:var(--white)}
.contact .divider::after{background:#2f2f2f}
.contact .divider::before,.contact .divider::after{border-color:#bbb}
.contact .divider::before{background:#bbb}
.info{left:157px;width:250px}
.info h5{font-size:14px;font-weight:400;display:flex;align-items:center;gap:10px}
.info p{font-size:12px;line-height:18px;margin:6px 0 0 26px;color:#eee}
.field{position:absolute;border:1px solid #999;background:rgba(0,0,0,.25);font-size:12px;color:#ddd;padding:8px 9px}
.copy{top:2828px;height:47px;background:var(--bar);color:var(--white);font-size:12px}
.social{right:157px;top:16px;display:flex;gap:12px}
.social i{display:block;width:14px;height:14px;border-radius:50%;background:var(--white)}
</style>
</head>
<body>

<header class="hero">
  <div class="abs" style="inset:0" role="img" aria-label="Harbour town seen across the water, boats moored along the quay, blue tint"></div>
  <div class="abs logo">Hensby Estates<span>Limited</span></div>
  <div class="abs burger"><i></i><i></i><i></i></div>
  <svg class="abs slide-arrow" style="left:0" viewBox="0 0 22 56"><path d="M14 20l-7 8 7 8" fill="none" stroke="#333" stroke-width="2.5"/></svg>
  <svg class="abs slide-arrow" style="left:1178px" viewBox="0 0 22 56"><path d="M8 20l7 8-7 8" fill="none" stroke="#333" stroke-width="2.5"/></svg>
  <div class="abs center hero-line1">Hensby Estates Limited (HEL) is a Family-owned Guernsey</div>
  <div class="abs center hero-line2">Property Holding Company</div>
  <div class="btn" style="left:537px;top:312px;width:126px;height:29px">Explore More</div>
</header>

<section class="about">
  <h2 class="abs center section-title" style="top:45px">About Us</h2>
  <div class="divider" style="top:78px"></div>
  <p class="abs center body-text" style="top:111px;left:300px;width:600px">Hensby Estates Limited (HEL) is a family-owned Guernsey property holding company. It purchases properties that are considered to have potential for development either through refurbishment or by obtaining planning permission to change its classification from, for example, industrial premises to offices or retail outlets, or by the marriage value of buying an adjacent property...</p>
  <div class="btn" style="left:537px;top:217px;width:126px;height:31px">Learn More</div>
</section>

<section class="band why">
  <div class="abs" style="inset:0" role="img" aria-label="Fishing boats in a harbour framed by dock structures, dark blue tint"></div>
  <h2 class="abs center section-title" style="top:70px">Why Guernsey?</h2>
  <p class="abs center body-text" style="top:111px;left:290px;width:620px">Hensby Estates Limited (HEL) is a family-owned Guernsey property holding company. It purchases properties that are considered to have potential for development either through refurbishment or by obtaining</p>
</section>
<svg class="notch" style="top:999px" viewBox="0 0 96 32"><path d="M0 0h96L48 32z" fill="#283d63"/></svg>

<section class="eras">
  <div class="era" style="left:147px">
    <h3>Yesterday</h3><div class="dots"></div>
    <p>HEL was founded in 1934 by Edmund Hensby to manage both his own extensive investments and his property portfolio in Guernsey...</p>
    <div class="more"><svg width="12" height="12" viewBox="0 0 12 12"><circle cx="6" cy="6" r="6" fill="#222"/><path d="M3 6h5M6 3.5L8.5 6 6 8.5" stroke="#fff" stroke-width="1.4" fill="none"/></svg>Read More</div>
  </div>
  <div class="era" style="left:450px">
    <h3>Today</h3><div class="dots"></div>
    <p>The Hensby family has steadily built on the foundations set out by the founder and each generation develops and manages the company...</p>
    <div class="more link"><svg width="12" height="12" viewBox="0 0 12 12"><circle cx="6" cy="6" r="6" fill="#4f84d6"/><path d="M3 6h5M6 3.5L8.5 6 6 8.5" stroke="#fff" stroke-width="1.4" fill="none"/></svg>Read More</div>
  </div>
  <div class="era" style="left:753px">
    <h3>Tomorrow</h3><div class="dots"></div>
    <p>In keeping with its past project development philosophy, its intrinsic understanding of the local property market and the successful...</p>
    <div class="more"><svg width="12" height="12" viewBox="0 0 12 12"><circle cx="6" cy="6" r="6" fill="#222"/><path d="M3 6h5M6 3.5L8.5 6 6 8.5" stroke="#fff" stroke-width="1.4" fill="none"/></svg>Read More</div>
  </div>
</section>

<section class="band blog-band">
  <div class="abs" style="inset:0" role="img" aria-label="Rocky islets and small boats on calm sea, blue tint"></div>
  <h2 class="abs center section-title" style="top:75px">Blog And Events</h2>
  <p class="abs center body-text" style="top:114px;left:240px;width:720px">There are many variations of passages of Lorem Ipsum available, but the majority have suffered alteration in some form, by injected humour, or randomised words which don't look even slightly believable. If you are going to use.</p>
</section>
<svg class="notch" style="top:1463px" viewBox="0 0 96 32"><path d="M0 0h96L48 32z" fill="#2b4a7a"/></svg>

<section class="posts">
  <article class="card" style="left:157px">
    <div class="photo" role="img" aria-label="Town houses on a hillside above a harbour" style="background:linear-gradient(180deg,#8fa9cf 0%,#9aa6ae 55%,#6f7a78 100%)"><div class="date">17<br>Aug</div></div>
    <h4>There are many variations available</h4>
    <div class="meta"><svg width="10" height="11" viewBox="0 0 10 11"><circle cx="5" cy="3" r="2.6" fill="#4f84d6"/><path d="M0 11c0-4 10-4 10 0z" fill="#4f84d6"/></svg>Quos Dolores</div>
    <p>Contrary to popular belief, Lorem Ipsum is simply random text. It has roots in a piece-classical Latin literature</p>
    <div class="more left"><svg width="12" height="12" viewBox="0 0 12 12"><circle cx="6" cy="6" r="6" fill="#222"/><path d="M3 6h5M6 3.5L8.5 6 6 8.5" stroke="#fff" stroke-width="1.4" fill="none"/></svg>Read More</div>
  </article>
  <article class="card" style="left:460px">
    <div class="photo" role="img" aria-label="Marina with snow-capped mountain and forest behind" style="background:linear-gradient(180deg,#9fb3c9 0%,#d9dde2 25%,#3f5a3f 55%,#6c7d8c 100%)"><div class="date">22<br>Aug</div></div>
    <h4>There are many variations available</h4>
    <div class="meta"><svg width="10" height="11" viewBox="0 0 10 11"><circle cx="5" cy="3" r="2.6" fill="#4f84d6"/><path d="M0 11c0-4 10-4 10 0z" fill="#4f84d6"/></svg>Quos Dolores</div>
    <p>Contrary to popular belief, Lorem Ipsum is simply random text. It has roots in a piece-classical Latin literature</p>
    <div class="more left link"><svg width="12" height="12" viewBox="0 0 12 12"><circle cx="6" cy="6" r="6" fill="#4f84d6"/><path d="M3 6h5M6 3.5L8.5 6 6 8.5" stroke="#fff" stroke-width="1.4" fill="none"/></svg>Read More</div>
  </article>
  <article class="card" style="left:765px">
    <div class="photo" role="img" aria-label="Crowded marina of sailing boats below green cliffs" style="background:linear-gradient(180deg,#6f96c8 0%,#8aa0a0 40%,#c9ced6 70%,#5f7690 100%)"><div class="date">26<br>Aug</div></div>
    <h4>There are many variations available</h4>
    <div class="meta"><svg width="10" height="11" viewBox="0 0 10 11"><circle cx="5" cy="3" r="2.6" fill="#4f84d6"/><path d="M0 11c0-4 10-4 10 0z" fill="#4f84d6"/></svg>Quos Dolores</div>
    <p>Contrary to popular belief, Lorem Ipsum is simply random text. It has roots in a piece-classical Latin literature</p>
    <div class="more left"><svg width="12" height="12" viewBox="0 0 12 12"><circle cx="6" cy="6" r="6" fill="#222"/><path d="M3 6h5M6 3.5L8.5 6 6 8.5" stroke="#fff" stroke-width="1.4" fill="none"/></svg>Read More</div>
  </article>

  <h2 class="abs center section-title events-title">Upcoming Events</h2>
  <div class="divider" style="top:507px"></div>

  <article class="event" style="left:155px">
    <div class="photo" role="img" aria-label="Harbour with pier and moored boats below a grassy headland" style="background:linear-gradient(180deg,#a9bedb 0%,#8d9a8a 35%,#3d5a78 65%,#6b7f4a 100%)"><div class="event-date">15 - Sept - 2016</div></div>
    <h4>The standard chunk of Lorem Ipsum used since</h4>
    <div class="meta"><svg width="10" height="11" viewBox="0 0 10 11"><circle cx="5" cy="3" r="2.6" fill="#4f84d6"/><path d="M0 11c0-4 10-4 10 0z" fill="#4f84d6"/></svg>Generate Humour</div>
    <p>It is a long established fact that a reader will be distracted by the rea a content of a page when looking at its layout.</p>
    <div class="more left"><svg width="12" height="12" viewBox="0 0 12 12"><circle cx="6" cy="6" r="6" fill="#222"/><path d="M3 6h5M6 3.5L8.5 6 6 8.5" stroke="#fff" stroke-width="1.4" fill="none"/></svg>Read More</div>
  </article>
  <article class="event" style="left:611px">
    <div class="photo" role="img" aria-label="Harbour with pier and moored boats below a grassy headland" style="background:linear-gradient(180deg,#a9bedb 0%,#8d9a8a 35%,#3d5a78 65%,#6b7f4a 100%)"><div class="event-date">22 - Sept - 2016</div></div>
    <h4>The standard chunk of Lorem Ipsum used since</h4>
    <div class="meta"><svg width="10" height="11" viewBox="0 0 10 11"><circle cx="5" cy="3" r="2.6" fill="#4f84d6"/><path d="M0 11c0-4 10-4 10 0z" fill="#4f84d6"/></svg>Generate Humour</div>
    <p>It is a long established fact that a reader will be distracted by the rea a content of a page when looking at its layout.</p>
    <div class="more left link"><svg width="12" height="12" viewBox="0 0 12 12"><circle cx="6" cy="6" r="6" fill="#4f84d6"/><path d="M3 6h5M6 3.5L8.5 6 6 8.5" stroke="#fff" stroke-width="1.4" fill="none"/></svg>Read More</div>
  </article>

  <div class="abs center pager">
    <svg width="20" height="10" viewBox="0 0 20 10"><path d="M20 5H2M6 1L2 5l4 4" stroke="#111" stroke-width="2" fill="none"/></svg>
    <span>/</span>
    <svg width="20" height="10" viewBox="0 0 20 10"><path d="M0 5h18M14 1l4 4-4 4" stroke="#4f84d6" stroke-width="1.5" fill="none"/></svg>
  </div>
</section>

<footer class="contact">
  <div class="abs" style="inset:0" role="img" aria-label="Harbour town at dusk with moored sailing boats, dark greyscale"></div>
  <h2 class="abs center section-title" style="top:42px">Get In Touch</h2>
  <div class="divider" style="top:78px"></div>
  <div class="abs info" style="top:120px">
    <h5><svg width="14" height="18" viewBox="0 0 14 18"><path d="M7 0a7 7 0 0 0-7 7c0 5 7 11 7 11s7-6 7-11a7 7 0 0 0-7-7z" fill="#fff"/><circle cx="7" cy="7" r="2.5" fill="#2a2a2a"/></svg>Address :</h5>
    <p>Sed ut perspiciatis unde omnis iste<br>commodi consequatur 123450</p>
  </div>
  <div class="abs info" style="top:201px">
    <h5><svg width="16" height="16" viewBox="0 0 16 16"><path d="M3.5 0.5l3 3.5-2 2.3c1 2 2.8 3.8 4.8 4.8l2.3-2 3.5 3-2 2.9C8 15 1 8 0.6 2.6z" fill="#fff"/></svg>Phone :</h5>
    <p>123-456-7890</p>
  </div>
  <div class="abs info" style="top:266px">
    <h5><svg width="16" height="12" viewBox="0 0 16 12"><rect width="16" height="12" fill="#fff"/><path d="M0 0l8 6 8-6" stroke="#2a2a2a" stroke-width="1.4" fill="none"/></svg>Email :</h5>
    <p style="color:#5b8fe0;text-decoration:underline">info@hensbyestateslimited.com</p>
  </div>
  <div class="field" style="left:460px;top:121px;width:280px;height:32px">Name :</div>
  <div class="field" style="left:763px;top:121px;width:280px;height:32px">Email :</div>
  <div class="field" style="left:460px;top:169px;width:583px;height:88px">Message :</div>
  <div class="btn" style="left:460px;top:274px;width:127px;height:31px;gap:6px"><svg width="12" height="12" viewBox="0 0 12 12"><path d="M12 0L0 5l4 2 1 5 2-3 3 2z" fill="#fff"/></svg>Send</div>
</footer>

<footer class="copy">
  <div class="abs" style="left:157px;top:16px">Copyright © 2016.&nbsp; Hensby Estates Limited.</div>
  <div class="abs social"><i></i><i></i><i></i><i></i></div>
</footer>

</body>
</html>
```